Valkemo App for Smart Devices IoT WiFi Electronic

Valkemo is a siren manufacturer. This application is used for the company's products that have a Wi-Fi connection and an internet connection, which can be configured and activated remotely through this application. In addition, this application is used to activate the siren at specific times for the start and end of shifts in companies and schools. Users will be siren installers and IT or HR managers.
In addition to activating motorized sirens timers, some siren models have speakers and allow you to play TTS (text to speech) audio, audio recorded by the user on the phone and upload audio (mp3) with playlist programming with start and end times.
Application screens: home with dashboard (one dashboard for each category). Device categories: timers, speakers, motorized siren. Screen for requesting evaluation in the Play Store. Screen for registering the user profile. Screen for registering devices according to their category (timers, speakers, motorized siren). Screen for registering device groups. Screen for pairing the device on the client's Wi-Fi network. Screen for registering activation times. Screen for uploading MP3 audios. Screen for registering playlists with audio selection, start and end times. Screen for recording audio for later sending to the speakers. Screen for converting text to speech and sending to the speakers. It is important to have a time picker with the day of the week to program the activation times and playlist.

Target Market(s)

Schools, Companies and Stores.

Industry/Entity Type

IoT

Font styles to use
Sans Serif
Other font styles liked:
• roboto

Colors
FFC000
F8CF3A
FAE287
FDF2CF
FEFAEE

Requirements
Must have
• time picker with weekdays for timer programming feature.
Nice to have
• app review request screen on play store

```html
<!DOCTYPE html>
<html lang="en">
<head>
<meta charset="utf-8">
<title>Valkemo – Siren App UI</title>
<link href="https://fonts.googleapis.com/css2?family=Source+Sans+3:wght@400;600;700&display=swap" rel="stylesheet">
<style>
:root{
  --bg:#F8D46E;
  --amber:#FFC000;
  --gold:#F8CF3A;
  --butter:#FAE287;
  --cream:#FDF2CF;
  --ivory:#FEFAEE;
  --white:#FFFFFF;
  --ink:#1E1E1E;
  --muted:#A7A7A7;
  --line:#EFC24A;
  --alert:#E0443A;
}
*{box-sizing:border-box;margin:0;padding:0}
html,body{width:1200px;height:1200px;overflow:hidden}
body{background:var(--bg);font-family:"Source Sans 3",sans-serif;color:var(--ink);position:relative}
.abs{position:absolute}
.screen{position:absolute;width:255px;border-radius:16px;background:var(--white);box-shadow:0 6px 18px rgba(160,110,0,.18);overflow:hidden}
.screen.warm{background:linear-gradient(180deg,var(--ivory),#FBF4DF)}
.screen.soft{background:#F8F8F6}

.brand{left:31px;top:216px;width:258px;height:64px;background:var(--cream);border-radius:6px;box-shadow:0 3px 8px rgba(160,110,0,.2);display:flex;align-items:center;justify-content:center}
.brand-name{font-size:56px;font-weight:700;color:var(--amber);letter-spacing:1px;line-height:1}
.tagline{left:42px;top:292px;width:250px;font-size:15px;line-height:18px}

.tabs{position:absolute;left:0;right:0;display:flex;justify-content:space-around;font-size:11px;font-weight:600;padding:0 12px}
.tabs span.active{color:var(--amber);border-bottom:1.5px solid var(--amber);padding-bottom:1px}

.dial{position:absolute}
.btn{position:absolute;height:22px;border-radius:6px;font-size:13px;display:flex;align-items:center;justify-content:center}
.btn.light{background:var(--butter)}
.btn.solid{background:var(--amber)}

.item{position:absolute;left:19px;width:217px;height:54px;background:var(--cream);border-radius:10px;display:flex;align-items:center;padding-left:12px}
.item .icon{width:38px;height:38px;flex:none}
.item .txt{margin-left:12px;line-height:15px}
.item .title{font-size:15px;font-weight:600}
.item .detail{font-size:12.5px}
.item .chev{position:absolute;right:12px;top:17px}
.item.more{padding-left:24px;font-size:13px}

.month-label{position:absolute;font-size:14px;font-weight:600}
.cal{position:absolute;display:grid;grid-template-columns:repeat(7,32.2px);grid-auto-rows:29px;font-size:14px}
.cal div{display:flex;align-items:center;justify-content:center;border:1px solid var(--line);margin:0 -1px -1px 0}
.cal div.empty{border-color:transparent}
.cal.boxed div{background:var(--gold);border-color:#F4C546}
.cal.boxed div.empty{background:transparent;border-color:transparent}
.pill{position:absolute;height:25px;border:1px solid var(--ink);border-radius:13px}

.schedule{position:absolute;left:0;width:255px;background:var(--gold)}
.sched-head{position:absolute;left:0;right:0;display:flex;justify-content:space-between;align-items:center;padding:0 12px;font-size:14px;font-weight:600}
.sched-head .arrow{font-size:22px;font-weight:400}
.row{position:absolute;left:7px;width:241px;height:30px}
.row .time{position:absolute;left:0;width:42px;height:30px;background:var(--cream);border-radius:6px;font-size:12.5px;display:flex;align-items:center;justify-content:center}
.row .name{position:absolute;left:52px;width:188px;height:30px;background:var(--cream);border-radius:6px;font-size:12.5px;display:flex;align-items:center;padding-left:9px}
.toggle{position:absolute;right:7px;top:8px;width:26px;height:12px;border-radius:6px;background:var(--ivory)}
.toggle::after{content:"";position:absolute;right:-2px;top:-2px;width:15px;height:15px;border-radius:50%;background:var(--gold);box-shadow:0 1px 2px rgba(0,0,0,.2)}
.toggle.off{background:#9D9D9D}
.toggle.off::after{right:auto;left:-2px}

.picker{position:absolute;left:0;width:255px}
.picker span{position:absolute;transform:translateX(-50%);white-space:nowrap}
.picker.dim{font-size:26px;color:var(--muted)}
.picker.main{font-size:28px}
.picker.main small{font-size:13px}
.reset{position:absolute;width:56px;height:56px;border-radius:50%;background:#ECECEC;display:flex;flex-direction:column;align-items:center;justify-content:center;font-size:12px;line-height:12px}
.reset small{font-size:7px;margin-top:2px}

.art{position:absolute;border-radius:14px;background:radial-gradient(circle at 45% 50%,#F8D45A 0%,#FBE59A 35%,var(--cream) 70%)}
</style>
</head>
<body>

<!-- brand -->
<div class="abs brand"><span class="brand-name">valkemo</span></div>
<p class="abs tagline">Best app to organize all your sirens. For offices, institutes etc. All of your needs in a app. Get connected with wifi and start an easy worry free life.</p>

<!-- timer screen -->
<section class="screen warm" style="left:342px;top:129px;height:447px">
  <nav class="tabs" style="top:43px"><span class="active">Timers</span><span>Speakers</span><span>Motorized Siren</span></nav>
  <svg class="dial" style="left:57px;top:154px" width="140" height="140" viewBox="0 0 140 140">
    <circle cx="70" cy="70" r="69" fill="#fff"/>
    <circle cx="70" cy="70" r="55" fill="none" stroke="#C9C9C9" stroke-width="6" stroke-dasharray="0.8 4.6"/>
    <path d="M66 15 A55 55 0 0 1 124 76" fill="none" stroke="var(--amber)" stroke-width="8" stroke-dasharray="1.6 2"/>
    <circle cx="124" cy="76" r="2.5" fill="var(--amber)"/>
    <text x="60" y="74" text-anchor="middle" font-size="12" font-family="Source Sans 3, sans-serif" fill="#1E1E1E">00 : 05 <tspan fill="var(--amber)">.24</tspan></text>
  </svg>
  <div class="btn light" style="left:14px;top:380px;width:107px">Reset</div>
  <div class="btn solid" style="left:136px;top:380px;width:106px">Resume</div>
</section>

<!-- siren list top -->
<section class="screen" style="left:625px;top:-16px;height:436px">
  <div class="item" style="top:16px"><svg class="icon" viewBox="0 0 38 38"><circle cx="19" cy="19" r="18" fill="#fff" stroke="var(--gold)" stroke-dasharray="1 2"/><path d="M17 13l6 6-6 6" fill="none" stroke="var(--alert)" stroke-width="1"/></svg><div class="txt"><div class="title">Siren name</div><div class="detail">Details</div></div><svg class="chev" width="14" height="18" viewBox="0 0 14 18"><path d="M2 2l10 7-10 7" fill="none" stroke="#8A8A8A" stroke-width="1.2"/></svg></div>
  <div class="item" style="top:90px"><svg class="icon" viewBox="0 0 38 38"><circle cx="19" cy="19" r="18" fill="#fff" stroke="var(--gold)" stroke-dasharray="1 2"/><path d="M17 13l6 6-6 6" fill="none" stroke="var(--alert)" stroke-width="1"/></svg><div class="txt"><div class="title">Siren name</div><div class="detail">Details</div></div><svg class="chev" width="14" height="18" viewBox="0 0 14 18"><path d="M2 2l10 7-10 7" fill="none" stroke="#8A8A8A" stroke-width="1.2"/></svg></div>
  <div class="item" style="top:163px"><svg class="icon" viewBox="0 0 38 38"><circle cx="19" cy="19" r="18" fill="#fff" stroke="var(--gold)" stroke-dasharray="1 2"/><path d="M17 13l6 6-6 6" fill="none" stroke="var(--alert)" stroke-width="1"/></svg><div class="txt"><div class="title">Siren name</div><div class="detail">Details</div></div><svg class="chev" width="14" height="18" viewBox="0 0 14 18"><path d="M2 2l10 7-10 7" fill="none" stroke="#8A8A8A" stroke-width="1.2"/></svg></div>
  <div class="item" style="top:237px"><svg class="icon" viewBox="0 0 38 38"><circle cx="19" cy="19" r="18" fill="#fff" stroke="var(--gold)" stroke-dasharray="1 2"/><path d="M17 13l6 6-6 6" fill="none" stroke="var(--alert)" stroke-width="1"/></svg><div class="txt"><div class="title">Siren name</div><div class="detail">Details</div></div><svg class="chev" width="14" height="18" viewBox="0 0 14 18"><path d="M2 2l10 7-10 7" fill="none" stroke="#8A8A8A" stroke-width="1.2"/></svg></div>
  <div class="item more" style="top:304px">More<svg class="chev" width="16" height="16" viewBox="0 0 16 16"><path d="M2 3l6 11 6-11" fill="none" stroke="#8A8A8A" stroke-width="1.2"/></svg></div>
</section>

<!-- standalone dial -->
<svg class="dial" style="left:967px;top:76px" width="140" height="140" viewBox="0 0 140 140">
  <circle cx="70" cy="70" r="69" fill="#fff" style="filter:drop-shadow(0 2px 3px rgba(160,110,0,.3))"/>
  <circle cx="70" cy="70" r="55" fill="none" stroke="#C9C9C9" stroke-width="6" stroke-dasharray="0.8 4.6"/>
  <path d="M66 15 A55 55 0 0 1 124 76" fill="none" stroke="var(--amber)" stroke-width="8" stroke-dasharray="1.6 2"/>
  <circle cx="124" cy="76" r="2.5" fill="var(--amber)"/>
  <text x="60" y="78" text-anchor="middle" font-size="12" font-family="Source Sans 3, sans-serif" fill="#1E1E1E">00 : 05 <tspan fill="var(--amber)">.24</tspan></text>
</svg>

<!-- standalone calendar -->
<div class="month-label" style="left:925px;top:236px">Month name</div>
<div class="cal boxed" style="left:925px;top:260px">
  <div class="empty"></div><div class="empty"></div><div>01</div><div>02</div><div>03</div><div>04</div><div>05</div>
  <div>06</div><div>07</div><div>08</div><div>09</div><div>10</div><div>11</div><div>12</div>
  <div>13</div><div>14</div><div>15</div><div>16</div><div>17</div><div>18</div><div>19</div>
  <div>20</div><div>21</div><div>22</div><div>23</div><div>24</div><div>25</div><div>26</div>
  <div>27</div><div>28</div><div>29</div><div>30</div>
</div>
<div class="pill" style="left:992px;top:291px;width:154px"></div>
<div class="pill" style="left:927px;top:320px;width:220px"></div>
<div class="pill" style="left:929px;top:348px;width:218px"></div>

<!-- calendar + schedule screen -->
<section class="screen" style="left:60px;top:460px;height:447px;background:#F8F8F6">
  <div class="month-label" style="left:16px;top:38px">Month name</div>
  <div class="cal" style="left:15px;top:60px">
    <div class="empty"></div><div class="empty"></div><div>01</div><div>02</div><div>03</div><div>04</div><div>05</div>
    <div>06</div><div>07</div><div>08</div><div>09</div><div>10</div><div>11</div><div>12</div>
    <div>13</div><div>14</div><div>15</div><div>16</div><div>17</div><div>18</div><div>19</div>
    <div>20</div><div>21</div><div>22</div><div>23</div><div>24</div><div>25</div><div>26</div>
    <div>27</div><div>28</div><div>29</div><div>30</div>
  </div>
  <div class="schedule" style="top:234px;height:213px;border-radius:14px 14px 0 0">
    <div class="sched-head" style="top:12px"><span class="arrow">&lt;</span><span>Month name</span><span class="arrow">&gt;</span></div>
    <div class="row" style="top:53px"><div class="time">08:10</div><div class="name">Siren name<span class="toggle"></span></div></div>
    <div class="row" style="top:92px"><div class="time">08:10</div><div class="name">Siren name<span class="toggle"></span></div></div>
    <div class="row" style="top:130px"><div class="time">08:10</div><div class="name">Siren name<span class="toggle"></span></div></div>
    <div class="row" style="top:168px"><div class="time">08:10</div><div class="name">Siren name<span class="toggle off"></span></div></div>
  </div>
</section>

<!-- motorized siren screen -->
<section class="screen soft" style="left:342px;top:624px;height:447px">
  <nav class="tabs" style="top:38px"><span>Timers</span><span>Speakers</span><span class="active">Motorized Siren</span></nav>
  <div class="picker dim" style="top:73px"><span style="left:51px">23</span><span style="left:127px">07</span><span style="left:205px">59</span></div>
  <div class="picker main" style="top:128px"><span style="left:54px">00<small>hour</small></span><span style="left:138px">08<small>min</small></span><span style="left:213px">00<small>sec</small></span></div>
  <div class="picker dim" style="top:182px"><span style="left:50px">01</span><span style="left:127px">09</span><span style="left:203px">01</span></div>
  <div class="reset" style="left:26px;top:231px">Reset<small>Reset</small></div>
  <div class="reset" style="left:100px;top:231px">Reset<small>Reset</small></div>
  <div class="reset" style="left:173px;top:231px">Reset<small>Reset</small></div>
  <div class="reset" style="left:26px;top:300px">Reset<small>Reset</small></div>
  <div class="btn solid" style="left:67px;top:395px;width:106px;font-size:12px">Start</div>
</section>

<!-- speaker screen -->
<section class="screen" style="left:625px;top:467px;height:447px;background:var(--ivory)">
  <nav class="tabs" style="top:43px"><span>Timers</span><span class="active">Speakers</span><span>Motorized Siren</span></nav>
  <div class="art" style="left:20px;top:85px;width:217px;height:169px" role="img" aria-label="Illustration of a speaker device with sound waves"></div>
  <div class="month-label" style="left:22px;top:265px">Speaker</div>
  <div class="item" style="top:301px"><svg class="icon" viewBox="0 0 38 38"><circle cx="19" cy="19" r="18" fill="#fff" stroke="var(--gold)" stroke-dasharray="1 2"/><path d="M17 13l6 6-6 6" fill="none" stroke="var(--alert)" stroke-width="1"/></svg><div class="txt"><div class="title">Siren name</div><div class="detail">Details</div></div><svg class="chev" width="14" height="18" viewBox="0 0 14 18"><path d="M2 2l10 7-10 7" fill="none" stroke="#8A8A8A" stroke-width="1.2"/></svg></div>
  <div class="item" style="top:365px"><svg class="icon" viewBox="0 0 38 38"><circle cx="19" cy="19" r="18" fill="#fff" stroke="var(--gold)" stroke-dasharray="1 2"/><path d="M17 13l6 6-6 6" fill="none" stroke="var(--alert)" stroke-width="1"/></svg><div class="txt"><div class="title">Siren name</div><div class="detail">Details</div></div><svg class="chev" width="14" height="18" viewBox="0 0 14 18"><path d="M2 2l10 7-10 7" fill="none" stroke="#8A8A8A" stroke-width="1.2"/></svg></div>
</section>

<!-- speakers list screen -->
<section class="screen" style="left:909px;top:460px;height:447px">
  <nav class="tabs" style="top:31px"><span>Timers</span><span class="active" style="border:none">Speakers</span><span>Motorized Siren</span></nav>
  <div class="item" style="top:72px"><svg class="icon" viewBox="0 0 38 38"><circle cx="19" cy="19" r="18" fill="#fff" stroke="var(--gold)" stroke-dasharray="1 2"/><path d="M17 13l6 6-6 6" fill="none" stroke="var(--alert)" stroke-width="1"/></svg><div class="txt"><div class="title">Siren name</div><div class="detail">Details</div></div></div>
  <div class="item" style="top:145px"><svg class="icon" viewBox="0 0 38 38"><circle cx="19" cy="19" r="19" fill="var(--amber)"/><path d="M17 13l6 6-6 6" fill="none" stroke="var(--alert)" stroke-width="1"/></svg><div class="txt"><div class="title">Siren name</div><div class="detail">Details</div></div></div>
  <div class="item" style="top:219px"><svg class="icon" viewBox="0 0 38 38"><circle cx="19" cy="19" r="19" fill="#A9A9A9"/><circle cx="19" cy="19" r="17" fill="none" stroke="#C4C4C4" stroke-dasharray="1 2"/><path d="M17 13l6 6-6 6" fill="none" stroke="var(--alert)" stroke-width="1"/></svg><div class="txt"><div class="title">Siren name</div><div class="detail">Details</div></div></div>
  <div class="item" style="top:292px"><svg class="icon" viewBox="0 0 38 38"><circle cx="19" cy="19" r="18" fill="#fff" stroke="var(--gold)" stroke-dasharray="1 2"/><path d="M17 13l6 6-6 6" fill="none" stroke="var(--alert)" stroke-width="1"/></svg><div class="txt"><div class="title">Siren name</div><div class="detail">Details</div></div></div>
  <div class="item more" style="top:359px">More</div>
</section>

<!-- schedule screen bottom -->
<section class="screen" style="left:625px;top:961px;height:260px">
  <div class="schedule" style="top:0;height:213px;border-radius:0 0 14px 14px">
    <div class="sched-head" style="top:16px"><span class="arrow">&lt;</span><span>Month name</span><span class="arrow">&gt;</span></div>
    <div class="row" style="top:56px"><div class="time">08:10</div><div class="name">Siren name<span class="toggle"></span></div></div>
    <div class="row" style="top:94px"><div class="time">08:10</div><div class="name">Siren name<span class="toggle"></span></div></div>
    <div class="row" style="top:133px"><div class="time">08:10</div><div class="name">Siren name<span class="toggle"></span></div></div>
    <div class="row" style="top:171px"><div class="time">08:10</div><div class="name">Siren name<span class="toggle"></span></div></div>
  </div>
</section>

</body>
</html>
```